Business Card Design

We Import cars and commercial vehicles, we have been in business around 12 years, we are based in Christchurch, New Zealand.
I really like the web address on card, possibly right along the bottom of the card?
We specialize in commercial vans, maybe worth a mention?
The logo has the name in it so probably don't need to have twice?

I really like a clean smart look, not too cluttered

Industry/Entity Type

Business

Contact Information for Business Card

RQL TOKYO IMPORTS, Derek Holloway, Managing Director
web address: www.rqlmotorsnz.com
cell phone. 021 485 912

Requirements
Must have
• the logo, and all the contact details.

Forgot to add my email address, derek@rqlmotorsnz.com
Nice to have
• Just thinking as the card is looking a little empty maybe somewhere written what we do? 'Specializing in commercial vans'
Not sure but we import Japanese vehicles, possibly adding some brands like Velkara Poremo Ketsu Brivon etc? Not sure on that one.

```html
<!DOCTYPE html>
<html lang="en">
<head>
<meta charset="utf-8">
<title>RQL Tokyo Imports – Business Card</title>
<link rel="stylesheet" href="https://fonts.googleapis.com/css2?family=Quicksand:wght@300;400;500;700&display=swap">
<style>
  :root {
    --stage: #e4e4e4;
    --card-top: #5e5e60;
    --card-band: #0d0d0d;
    --cell-line: #5a5a5a;
    --ink-dark: #0a0a0a;
    --ink-light: #ffffff;
    --ink-muted: #c9c9c9;
    --van-light: #f2f2f2;
    --van-shade: #8a8a8a;
  }
  * { box-sizing: border-box; margin: 0; padding: 0; }
  html, body {
    width: 1200px; height: 900px; overflow: hidden;
    background: var(--stage);
    font-family: "Quicksand", sans-serif;
  }
  .stage {
    width: 1200px; height: 900px;
    display: flex; align-items: center; justify-content: center;
  }
  .card {
    position: relative;
    width: 1050px; height: 600px;
    background: var(--card-top);
    overflow: hidden;
    box-shadow: 0 10px 30px rgba(0,0,0,0.18);
  }
  .brand {
    position: absolute; left: 150px; top: 52px;
    display: flex; align-items: center; gap: 20px;
  }
  .brand-name {
    color: var(--ink-dark);
    font-weight: 700;
    font-size: 74px;
    line-height: 0.9;
    letter-spacing: 1px;
    text-transform: uppercase;
  }
  .brand-vehicle {
    width: 250px; height: 170px;
  }
  .person {
    position: absolute; left: 330px; top: 238px;
    color: var(--ink-light);
  }
  .person-name {
    font-size: 54px; font-weight: 300; letter-spacing: -0.5px;
  }
  .person-name strong { font-weight: 700; }
  .person-role {
    margin-top: 2px; margin-left: 140px;
    font-size: 22px; font-weight: 400; color: var(--ink-muted);
  }
  .contact-band {
    position: absolute; left: 0; right: 0; bottom: 0; height: 240px;
    background: var(--card-band);
    display: flex; padding: 18px 22px;
  }
  .contact-item {
    flex: 1;
    border: 1px solid var(--cell-line);
    display: flex; flex-direction: column; align-items: center; justify-content: center;
    gap: 30px;
    color: var(--ink-light);
    font-size: 25px; font-weight: 400;
  }
  .contact-item + .contact-item { border-left: none; }
  .contact-item.email { flex: 1.3; }
  .contact-item.phone { flex: 1; }
  .contact-item.web { flex: 1.35; }
  .contact-icon { width: 58px; height: 58px; }
</style>
</head>
<body>
<main class="stage">
  <section class="card">
    <header class="brand">
      <div class="brand-name">RQL Tokyo<br>Imports</div>
      <svg class="brand-vehicle" viewBox="0 0 250 170" role="img" aria-label="Illustration of a white commercial van">
        <defs>
          <linearGradient id="vanTone" x1="0" y1="0" x2="0" y2="1">
            <stop offset="0" stop-color="var(--van-light)"/>
            <stop offset="1" stop-color="var(--van-shade)"/>
          </linearGradient>
        </defs>
        <rect x="0" y="0" width="250" height="170" rx="18" fill="url(#vanTone)"/>
      </svg>
    </header>

    <div class="person">
      <h1 class="person-name">Derek <strong>Holloway</strong></h1>
      <p class="person-role">Managing Director</p>
    </div>

    <footer class="contact-band">
      <div class="contact-item email">
        <svg class="contact-icon" viewBox="0 0 58 58" aria-hidden="true">
          <circle cx="29" cy="29" r="26" fill="none" stroke="#fff" stroke-width="2"/>
          <rect x="18" y="21" width="22" height="16" rx="1.5" fill="#fff"/>
          <path d="M18 22 L29 31 L40 22" fill="none" stroke="#0d0d0d" stroke-width="1.8"/>
        </svg>
        <span>derek@rqlmotorsnz.com</span>
      </div>
      <div class="contact-item phone">
        <svg class="contact-icon" viewBox="0 0 58 58" aria-hidden="true">
          <circle cx="29" cy="29" r="26" fill="none" stroke="#fff" stroke-width="2"/>
          <rect x="22" y="16" width="14" height="26" rx="2.5" fill="none" stroke="#fff" stroke-width="2"/>
          <circle cx="29" cy="38" r="1.5" fill="#fff"/>
        </svg>
        <span>021 485 912</span>
      </div>
      <div class="contact-item web">
        <svg class="contact-icon" viewBox="0 0 58 58" aria-hidden="true">
          <circle cx="29" cy="29" r="26" fill="none" stroke="#fff" stroke-width="2"/>
          <circle cx="29" cy="29" r="12" fill="none" stroke="#fff" stroke-width="2"/>
          <ellipse cx="29" cy="29" rx="5" ry="12" fill="none" stroke="#fff" stroke-width="1.6"/>
          <line x1="17" y1="29" x2="41" y2="29" stroke="#fff" stroke-width="1.6"/>
        </svg>
        <span>www.rqlmotorsnz.com</span>
      </div>
    </footer>
  </section>
</main>
</body>
</html>
```